Pelmora Swifts Stridefair - 2 posters

We need two community event posters for an annual marathon with continuity in design showcasing the clubs logo colours and community spirit. Poster one is for the Juniors division which needs to look like a fun day encouraging families to come down and register and compete. It will be distributed to all the schools and social media. Poster two is for the main event again attracting registration with prizes. Encouraging all levels of runners from professionals to amateurs family friendly. It is in a unique location along the city's foreshore with amazing views.

Target Market(s)

Marathon runners, juniors, community and families

Requirements
Must have
• photos, logos details
Nice to have
• We are looking for a motivating high energy poster to entice registration and feel like fun event for the whole comminty

```html
<!DOCTYPE html>
<html lang="en">
<head>
<meta charset="utf-8">
<title>Swifts Junior Stridefair 2018</title>
<link href="https://fonts.googleapis.com/css2?family=Montserrat:wght@500;700;800;900&display=swap" rel="stylesheet">
<style>
  :root{
    --red:#e3101f;
    --orange:#f07a14;
    --yellow:#f6e51c;
    --blue:#1f8fd0;
    --navy:#1f3f8f;
    --teal:#7fd9d8;
    --ink:#111;
    --white:#fff;
  }
  *{margin:0;padding:0;box-sizing:border-box}
  html,body{width:849px;height:1200px;overflow:hidden;background:var(--white)}
  body{font-family:"Montserrat",sans-serif;color:var(--ink)}
  .poster{position:relative;width:849px;height:1200px;overflow:hidden;background:var(--white)}
  .backdrop{position:absolute;inset:0}
  .event-brand{position:absolute;left:34px;top:36px;width:248px;height:84px;display:flex;align-items:center;gap:10px}
  .event-brand .dot{width:22px;height:22px;border-radius:50%;background:var(--orange);flex:none}
  .event-brand span{font-weight:800;font-size:22px;line-height:1.05;color:var(--white)}
  .title{position:absolute;left:36px;top:160px;width:790px;font-weight:900;line-height:1}
  .title .year{color:var(--red);font-size:98px;letter-spacing:-1px;vertical-align:baseline}
  .title .club{font-size:64px;margin-left:14px}
  .title .line2{display:block;font-size:62px;text-align:right;margin-top:-6px;padding-right:10px}
  .photo{position:absolute;left:292px;top:330px;width:270px;height:760px}
  .tagline{position:absolute;left:38px;top:384px;font-weight:800;font-size:52px;line-height:64px}
  .bang{position:absolute;left:140px;top:770px;font-weight:900;font-size:100px;line-height:1}
  .register{position:absolute;left:36px;top:890px;font-size:19px;font-weight:500;line-height:29px}
  .register b{font-weight:800;font-size:21px}
  .date{position:absolute;left:566px;top:780px;width:250px;font-weight:900;line-height:1}
  .date .day{font-size:38px;display:block;letter-spacing:1px}
  .date .month{font-size:40px;display:block;margin-top:8px}
  .date .month b{font-size:62px;font-weight:900;margin-left:6px}
  .venue{position:absolute;left:560px;top:905px;width:264px;text-align:center;font-weight:800;font-size:16px;line-height:21px}
  .races{position:absolute;left:556px;top:962px;width:268px;text-align:center;font-weight:800;font-size:12.6px;line-height:16.5px}
  .partner{position:absolute;display:flex;align-items:center;justify-content:center;gap:8px}
  .partner span{font-weight:800;color:var(--white)}
  .partner .dot{width:14px;height:14px;border-radius:50%;background:var(--white);flex:none}
  .club-mark{left:36px;top:1032px;width:66px;height:68px;background:var(--white);border-radius:4px}
  .club-mark .dot{width:46px;height:46px;background:var(--red)}
  .health-partner{left:108px;top:1032px;width:184px;height:68px;background:var(--white)}
  .health-partner span{color:var(--navy);font-size:19px}
  .photo-partner{left:574px;top:1034px;width:234px;height:68px;background:#000}
  .photo-partner span{font-size:17px}
  .sponsors{position:absolute;left:20px;top:1108px;width:809px;text-align:center;font-weight:700;font-size:11.2px;line-height:14.8px;color:var(--ink)}
  .tags{position:absolute;left:0;top:1173px;width:849px;text-align:center;font-weight:700;font-size:11.2px}
</style>
</head>
<body>
<div class="poster">
  <svg class="backdrop" width="849" height="1200" viewBox="0 0 849 1200" aria-hidden="true">
    <rect width="849" height="1200" fill="var(--orange)"/>
    <path d="M0 0H560C400 60 180 170 0 330Z" fill="var(--blue)"/>
    <path d="M120 0H600C420 50 260 130 60 300C100 180 110 80 120 0Z" fill="var(--teal)"/>
    <path d="M330 0H640C470 80 250 190 20 330C140 200 250 90 330 0Z" fill="var(--yellow)"/>
    <path d="M560 0H849V260C790 140 690 50 560 0Z" fill="var(--red)"/>
    <path d="M680 0H849V120C800 60 740 20 680 0Z" fill="#1a8f7a"/>
    <path d="M0 1200V1000C250 880 600 870 849 820V1200Z" fill="var(--red)"/>
    <path d="M0 1200V1060C300 1000 620 1020 849 960V1200Z" fill="var(--blue)"/>
    <path d="M200 1200C400 1120 650 1070 849 1000V1200Z" fill="var(--navy)"/>
    <path d="M380 1200C560 1140 720 1080 849 1040V1200Z" fill="var(--orange)"/>
    <path d="M560 1200C680 1150 780 1110 849 1090V1200Z" fill="var(--yellow)"/>
    <path d="M849 760C840 840 800 900 740 960C800 940 840 880 849 840Z" fill="var(--yellow)"/>
    <path d="M0 340C180 180 430 70 650 0C760 40 830 140 849 280V770C700 850 400 880 0 1000Z" fill="var(--white)"/>
    <path d="M0 1000C300 930 600 880 849 780" fill="none" stroke="var(--orange)" stroke-width="8" opacity=".6"/>
  </svg>

  <div class="event-brand" style="background:var(--blue);border-radius:6px;padding:0 12px">
    <span class="dot"></span><span>Pelmora Swifts Stridefair</span>
  </div>

  <h1 class="title">
    <span class="year">2018</span><span class="club">SWIFTS</span>
    <span class="line2">JUNIOR STRIDEFAIR</span>
  </h1>

  <svg class="photo" viewBox="0 0 270 760" role="img" aria-label="Photo of a young runner in a bucket hat and race bib leaping forward with arms outstretched">
    <defs>
      <linearGradient id="photoTone" x1="0" y1="0" x2="0" y2="1">
        <stop offset="0" stop-color="#2a3f5c"/>
        <stop offset=".45" stop-color="#b8bfc6"/>
        <stop offset=".75" stop-color="#2f6f95"/>
        <stop offset="1" stop-color="#d9b89a"/>
      </linearGradient>
    </defs>
    <rect x="4" y="4" width="262" height="752" rx="60" fill="url(#photoTone)" stroke="var(--yellow)" stroke-width="6"/>
  </svg>

  <p class="tagline">GREAT<br>PRIZES<br>&amp; FUN<br>FOR THE<br>WHOLE<br>FAMILY</p>
  <p class="bang">!</p>
  <p class="register">Don’t miss out register at<br><b>pelmorastridefair.com</b></p>

  <p class="date"><span class="day">SATURDAY</span><span class="month">JUNE<b>30</b></span></p>
  <p class="venue">FORESHORE<br>PELMORA YACHT CLUB</p>
  <p class="races">RACES START 4.00PM<br>1 MILE (1.6KM) 3-6 YEARS OLD<br>2 MILES (3.2KM) 7-11 YEARS OLD<br>3 MILES (4.8KM) 12-16 YEARS OLD</p>

  <div class="partner club-mark" role="img" aria-label="Pelmora Swifts Club"><span class="dot"></span></div>
  <div class="partner health-partner"><span>Northwind Health</span></div>
  <div class="partner photo-partner"><span class="dot"></span><span>Halo Events &amp; Photography</span></div>

  <p class="sponsors">Pelmora Swifts Club presents this event to the Community with thanks to generous Sponsors, Partners and Volunteers including:<br>KTR Electrical | The Runner’s Sole | Bayline Fireworks | The Harbourview Apartments | Toastie Hut | Marlo Reed Jewellers | Core Forty<br>Pelmora Motors | Dana Corrie MLA | Crema Cafe | Ivy Hollis Naturopathics | Fuelstop West | Pharmacy 27 | Sport Central<br>Stepwell Podiatry | Harlow &amp; Finch | Coastal Rescue | Brent Oakes Homes | Sunbay Print |</p>
  <p class="tags">#swiftsstridefair #welovemarathons #fitnessforlife</p>
</div>
</body>
</html>
```